Monument sign* - Law Firm

*I am installing a monument sign that has LED, as well as backlit elements. I am seeking help in designing the backlit portion of the sign. The Backlit sign will be 12’ x 4’.

We are looking for a classic, yet eye-catching sign to help new and current clients find our firm as well as bring in future clients. One of our goals is that people who drive by on a regular basis remember our sign (and us) for any future legal need.

Target Market(s)

Current and future clientele

Industry/Entity Type

Law Firm

Font styles to use
Serif
Sans Serif

Colors
b1b1b1
333333

Requirements
Must have
• Business name: Hartwell Law Firm, Inc.
• Website: www.hartwelllawfirm-example.com
• Telephone: (555)274-1936
• Our firm's logo
Nice to have
• Color preference is black, taupe, and white. A photo for reference of the office coloring is uploaded.
• We currently have an established logo which our firm has been using for more than 10 years. Our logo has been used in advertising, commercials, letterhead, and on-site. We are looking to transition from brown/rust/cream to the black/taupe/white color scheme.
Should not have
• Cheesy slogans; character designs; directions; additional symbols outside of the firm's logo.

```html
<!DOCTYPE html>
<html lang="en">
<head>
<meta charset="utf-8">
<title>Hartwell Law Firm — Monument Sign</title>
<link href="https://fonts.googleapis.com/css2?family=Cinzel:wght@400;500&display=swap" rel="stylesheet">
<style>
  :root {
    --backdrop: #776d69;
    --sign-white: #ffffff;
    --ink: #2b2b2b;
    --copper: #bf743e;
    --shadow: rgba(40, 34, 32, 0.45);
  }
  * { margin: 0; padding: 0; box-sizing: border-box; }
  html, body {
    width: 1200px; height: 1000px; overflow: hidden;
    background: var(--backdrop);
    font-family: "Cinzel", "Times New Roman", serif;
  }
  .sign {
    position: absolute; left: 70px; top: 323px;
    width: 1060px; height: 354px;
    background: var(--sign-white);
    box-shadow: 14px 12px 10px var(--shadow);
    overflow: hidden;
  }
  .brand-mark {
    position: absolute; left: 28px; top: 28px;
    width: 237px; height: 297px;
    background: var(--copper);
  }
  .brand-name {
    position: absolute; left: 268px; top: 28px;
    width: 32px; height: 297px;
    display: flex; align-items: center; justify-content: center;
    overflow: hidden;
  }
  .brand-name span {
    display: block;
    transform: rotate(90deg);
    white-space: nowrap;
    font-size: 19px; font-weight: 500;
    letter-spacing: 2px;
    line-height: 1;
    color: var(--ink);
  }
  .name-band {
    position: absolute; left: 323px; top: 28px;
    width: 710px; height: 112px;
    background: var(--ink);
    display: flex; align-items: center; justify-content: center;
  }
  .firm-name {
    font-size: 50px; font-weight: 400;
    color: var(--sign-white);
    letter-spacing: 1px;
    white-space: nowrap;
  }
  .contact-frame {
    position: absolute; left: 323px; top: 140px;
    width: 710px; height: 182px;
    border: 3px solid var(--ink);
    border-top: none;
  }
  .phone-panel {
    position: absolute; left: 11px; top: 14px;
    width: 682px; height: 143px;
    background: var(--copper);
    display: flex; align-items: center; justify-content: center;
  }
  .phone {
    font-size: 74px; font-weight: 400;
    color: var(--sign-white);
    letter-spacing: 9px;
    white-space: nowrap;
  }
  .website {
    position: absolute; left: 50%; bottom: -12px;
    transform: translateX(-50%);
    background: var(--sign-white);
    padding: 0 8px;
    font-size: 17px; font-weight: 500;
    letter-spacing: 2px;
    line-height: 1.2;
    color: var(--ink);
    white-space: nowrap;
  }
</style>
</head>
<body>
  <div class="sign">
    <div class="brand-mark" aria-hidden="true"></div>
    <div class="brand-name"><span>HARTWELL LAW FIRM</span></div>
    <div class="name-band">
      <h1 class="firm-name">Hartwell Law Firm, Inc.</h1>
    </div>
    <div class="contact-frame">
      <div class="phone-panel">
        <p class="phone">(555)274-1936</p>
      </div>
      <p class="website">WWW.HARTWELLLAWFIRM-EXAMPLE.COM</p>
    </div>
  </div>
</body>
</html>
```